Need a clean & modern homepage for an education site + opportunity for longer term work

Thanks for viewing our project. We are excited about this new website and we hope that we might build a relationship with designers as we work on this project. I provided quite a few details and requirements to help you more quickly create a design that meets our needs.
Who we are:
We are a website that discusses the importance of college accreditation and provides a directory of college programs.
What we need:
A homepage that meets the below requirements and is inspired by the examples provided
Definition of accredited:
ac·cred·it·ed [uh-kred-i-tid] adj.
1. officially recognized as meeting the essential requirements, as of academic excellence: accredited schools.
2. provided with official credentials, as by a government: an accredited diplomatic representative.
3. accepted as authoritative: an accredited theory.
Overall look and feel for the homepage:
- Clean, simple and modern
- Limited (or zero) pictures
- Utilize color blocks with text
- A trend seems to be longer vertical length homepages with lots of whitespace. I generally like this trend as long as the page is not way to tall.
Inspirations: Sites that have a similar look and feel to what I need.
http://lernvista.org/
http://www.campusmetrix.com/colleges/orlen-university/
http://quietmarrow.org/
http://www.velmoratalent.com/
http://www.pluvo.com/
http://sketches.zumo.com/
Items to be included on the homepage. Details below on each item.
- Top navigation
- Logo: Please leave a blank area for a logo. The logo has not been designed.
- Simple graphic/color block at the top that highlights a definition of “Accredited” – the definition should be formatted like it is being copy/pasted from a dictionary.
- Space for a video and small (50 word) written description of the video. You can use placeholder text.
- One section with 3 Paragraphs of content (each paragraph around 100 words) with a header at the top. You can use placeholder text but please create the formatting. At the end of the 3 paragraphs please have a “Read More” Note this shouldn't be 3 separate paragraphs with three read mores - it is 3 paragraphs with one read more at the end.
- An area with the header “Search Colleges by State” that has anchor text links to all 50 states.
Top navigation:
- Home
- States – with a subnav dropdown that includes all 50 US states.
- Programs – with a subnav dropdown that includes program titles (list below)
- Degrees - with a subnav dropdown that includes 5 degree levels (list below)
- Accreditation – no subnav
- Rankings – no subnav
- Resources – no subnav
Footer
- Link to about us, privacy, and a copyright www.url.com
Programs List for sub navigation
Accounting
Art
Bible
Business
Criminal Justice
Design
Engineering
English
Law
LPN to RN
Management
Math
MBA
MPH
Medical Assisting
Military
Nursing
Occupational Therapy
Paralegal
Psychology
Pharmacy
RN to BSN
Radiology
Social Work
Sonography
Degrees list for sub navigation
Certificate
Associate
Bachelors
Masters
PhD
Thanks so much - looking forward to working with you!

```html
<!DOCTYPE html>
<html lang="en">
<head>
<meta charset="utf-8">
<title>Accredited – College Accreditation Directory</title>
<link rel="stylesheet" href="https://fonts.googleapis.com/css2?family=Ubuntu:wght@400;500&family=Ubuntu+Mono&display=swap">
<style>
:root{
  --ink:#000;
  --nav:#151515;
  --pink:#e0053f;
  --pink-dark:#cc0039;
  --orange:#ff9000;
  --white:#fff;
  --paper:#fcfcfc;
  --grey-bg:#ebebee;
  --grey-light:#f2f2f4;
  --grey-panel:#dedcdc;
  --text:#4a4a4a;
  --video:#000;
}
*{box-sizing:border-box;margin:0;padding:0}
html,body{width:1099px;height:1200px;overflow:hidden;background:var(--white)}
body{position:relative;font-family:"Ubuntu",Arial,sans-serif;color:var(--text)}
a{text-decoration:none;color:inherit}

.site-header{position:absolute;left:0;top:0;width:1099px;height:79px;background:var(--ink)}
.brand{position:absolute;left:214px;top:16px;color:var(--white)}
.brand-name{font-size:31px;line-height:34px}
.brand-name span{color:var(--pink)}
.brand-slogan{font-size:16px;line-height:20px;margin-top:2px}
.follow{position:absolute;left:803px;top:51px;display:flex;align-items:center;gap:6px;color:#bbb;font-size:8px}
.follow .social{width:13px;height:13px;background:var(--white)}
.follow .social.first{background:var(--pink);margin-left:8px}

.main-nav{position:absolute;left:0;top:79px;width:1099px;height:59px;background:var(--nav)}
.main-nav a{position:absolute;top:23px;color:var(--white);font-size:11px;line-height:13px;white-space:nowrap}
.main-nav a.active{color:var(--pink)}
.main-nav .dot{display:inline-block;width:6px;height:6px;border-radius:50%;background:var(--white);margin-left:9px;vertical-align:1px}
.main-nav .sep{position:absolute;top:22px;width:1px;height:16px;background:#3a3a3a}

.hero{position:absolute;left:0;top:138px;width:1099px;height:279px;background:var(--pink);overflow:hidden}
.hero svg.bg{position:absolute;left:0;top:0}
.hero-badge{position:absolute;left:215px;top:70px;width:168px;height:168px;border-radius:50%;background:radial-gradient(circle at 45% 50%,#d4141c 0,#d4141c 14%,#e8e2d2 30%,#f4f1ea 55%,#fff 75%)}
.definition{position:absolute;left:392px;top:106px;width:366px;text-align:center;color:var(--white)}
.definition .word{font-family:"Ubuntu Mono",monospace;font-size:26px;line-height:30px;color:#111;letter-spacing:-0.5px}
.definition .sense{font-size:10.5px;line-height:15px;margin-top:20px}
.cta-state{position:absolute;z-index:5;left:724px;top:397px;width:150px;height:36px;background:var(--orange);color:var(--white);font-size:11.5px;line-height:36px;text-align:center}

.video-section{position:absolute;left:0;top:417px;width:1099px;height:223px;background:var(--white)}
.video-heading{position:absolute;left:214px;top:37px;font-size:13.5px;font-weight:400;color:#444}
.video-copy{position:absolute;left:214px;top:100px;width:360px;font-size:8.3px;line-height:10px;color:#333}
.video-copy p+p{margin-top:9px}
.video-copy .accent{color:var(--pink)}
.video-player{position:absolute;left:597px;top:38px;width:277px;height:156px;background:var(--video)}
.video-controls{position:absolute;left:4px;bottom:4px;right:4px;height:20px;display:flex;align-items:center;gap:6px}
.play{width:32px;height:20px;background:#1c1c1c;display:flex;align-items:center;justify-content:center}
.track{flex:1;height:20px;background:#1c1c1c;display:flex;align-items:center;padding:0 4px;gap:4px}
.track b{flex:1;height:4px;border:1px solid #3a3a3a;border-radius:2px}
.track em{font-style:normal;font-size:7px;color:#1aa0e0;font-weight:500}

.features{position:absolute;left:0;top:640px;width:1099px;height:478px;background:var(--grey-bg);overflow:hidden}
.features svg.bg{position:absolute;left:0;top:0}
.feature{position:absolute;left:214px;width:660px;height:119px;display:flex}
.feature-head{width:168px;height:100%;background:var(--grey-panel);position:relative;color:#111;font-size:12.5px;text-align:center}
.feature-head .label{position:absolute;left:0;right:0;top:70px}
.feature-head svg{position:absolute;left:62px;top:14px}
.feature-head::after{content:"";position:absolute;right:-6px;top:54px;border:6px solid transparent;border-left-color:var(--grey-panel);border-right:0}
.feature-body{flex:1;background:var(--paper);position:relative;padding:24px 32px 0 32px;font-size:7.5px;line-height:9px;color:#555}
.feature-body p+p{margin-top:9px}
.read-more{position:absolute;right:30px;bottom:7px;width:76px;height:25px;background:var(--pink);color:var(--white);font-size:8px;line-height:25px;text-align:center}
.feature.highlight .feature-head{background:var(--pink-dark);color:var(--white)}
.feature.highlight .feature-head::after{border-left-color:var(--pink-dark)}
.feature.highlight .feature-body{background:var(--pink);color:var(--white)}
.feature.highlight .read-more{background:var(--white);color:var(--pink)}

.site-footer{position:absolute;left:0;top:1118px;width:1099px;height:82px;background:var(--ink);color:var(--white);font-size:7.5px}
.footer-nav a{position:absolute;top:36px}
.footer-nav a.active{color:var(--pink)}
.footer-nav .sep{position:absolute;top:33px;width:1px;height:13px;background:#444}
.copyright{position:absolute;left:0;right:0;top:58px;text-align:center;font-size:6.5px}
</style>
</head>
<body>

<header class="site-header">
  <div class="brand">
    <div class="brand-name">Your <span>Logo</span></div>
    <div class="brand-slogan">Slogan Goes Here</div>
  </div>
  <div class="follow">Follow Us <span class="social first"></span><span class="social"></span></div>
</header>

<nav class="main-nav">
  <a class="active" href="#" style="left:215px">Home</a>
  <span class="sep" style="left:292px"></span>
  <a href="#" style="left:325px">States<span class="dot"></span></a>
  <span class="sep" style="left:393px"></span>
  <a href="#" style="left:421px">Programs<span class="dot"></span></a>
  <span class="sep" style="left:490px"></span>
  <a href="#" style="left:520px">Degrees<span class="dot"></span></a>
  <span class="sep" style="left:585px"></span>
  <a href="#" style="left:614px">Accreditation</a>
  <span class="sep" style="left:698px"></span>
  <a href="#" style="left:724px">Resources</a>
  <span class="sep" style="left:800px"></span>
  <a href="#" style="left:835px">Rankings</a>
</nav>

<section class="hero">
  <svg class="bg" width="1099" height="279" aria-hidden="true">
    <polygon points="0,0 150,0 420,279 0,279" fill="#d8033c" opacity="0.6"/>
    <polygon points="690,0 1099,0 1099,279 910,279 750,110 760,100" fill="var(--pink-dark)"/>
  </svg>
  <div class="hero-badge" role="img" aria-label="Rolled diploma tied with a red ribbon"></div>
  <div class="definition">
    <div class="word">ac·cred·it·ed</div>
    <div class="sense">(a person, organization, or course of study) Officially recognized or authorized:<br>"an accredited chiropractic school".</div>
  </div>
</section>

<section class="video-section">
  <h2 class="video-heading">Heading of Video</h2>
  <div class="video-copy">
    <p>Lorem Ipsum is simply dummy text of the printing and typesetting industry. Lorem Ipsum has been the industry's standard dummy text ever since the 1500s, when an unknown printer took a galley of type and scrambled it to make a type specimen book.</p>
    <p><span class="accent">Lorem Ipsum is simply dummy text</span> of the printing and typesetting industry.</p>
  </div>
  <div class="video-player">
    <div class="video-controls">
      <span class="play"><svg width="10" height="10"><polygon points="1,0 10,5 1,10" fill="var(--pink)"/></svg></span>
      <span class="track"><b></b><em>||||| HD ⁘</em></span>
    </div>
  </div>
</section>

<a class="cta-state" href="#">Search Colleges by State</a>

<section class="features">
  <svg class="bg" width="1099" height="478" aria-hidden="true">
    <polygon points="215,0 680,0 1099,360 1099,478 560,478" fill="var(--grey-light)"/>
    <polygon points="680,0 760,0 1099,290 1099,360" fill="#e4e4e8"/>
  </svg>

  <article class="feature" style="top:33px">
    <div class="feature-head">
      <svg width="44" height="46" aria-hidden="true"><rect x="6" y="24" width="24" height="14" transform="skewX(-20)" fill="none" stroke="#111" stroke-width="3"/><path d="M8 26 L18 34 L38 4" fill="none" stroke="#d0021b" stroke-width="5" stroke-linecap="round"/></svg>
      <div class="label">Lorem Ipsum is simply</div>
    </div>
    <div class="feature-body">
      <p>Lorem Ipsum is simply dummy text of the printing and typesetting industry. Lorem Ipsum has been the industry's standard dummy text ever since the 1500s</p>
      <p>when an unknown printer took a galley of type and scrambled it to make a type specimen book. Lorem Ipsum is simply dummy text of the printing and typesetting industry. Lorem Ipsum has been the industry's standard dummy text ever since the 1500s</p>
      <a class="read-more" href="#">+read more</a>
    </div>
  </article>

  <article class="feature highlight" style="top:172px">
    <div class="feature-head">
      <svg width="44" height="46" aria-hidden="true"><polygon points="2,20 42,4 30,38 20,26" fill="#fff"/><polygon points="20,26 42,4 22,34" fill="#ddd"/></svg>
      <div class="label">Lorem Ipsum is simply</div>
    </div>
    <div class="feature-body">
      <p>Lorem Ipsum is simply dummy text of the printing and typesetting industry. Lorem Ipsum has been the industry's standard dummy text ever since the 1500s</p>
      <p>when an unknown printer took a galley of type and scrambled it to make a type specimen book. Lorem Ipsum is simply dummy text of the printing and typesetting industry. Lorem Ipsum has been the industry's standard dummy text ever since the 1500s</p>
      <a class="read-more" href="#">+read more</a>
    </div>
  </article>

  <article class="feature" style="top:316px">
    <div class="feature-head">
      <svg width="44" height="46" aria-hidden="true"><rect x="6" y="24" width="24" height="14" transform="skewX(-20)" fill="none" stroke="#111" stroke-width="3"/><path d="M8 26 L18 34 L38 4" fill="none" stroke="#d0021b" stroke-width="5" stroke-linecap="round"/></svg>
      <div class="label" style="top:56px">Lorem Ipsum is simply</div>
    </div>
    <div class="feature-body">
      <p>Lorem Ipsum is simply dummy text of the printing and typesetting industry. Lorem Ipsum has been the industry's standard dummy text ever since the 1500s</p>
      <p>when an unknown printer took a galley of type and scrambled it to make a type specimen book. Lorem Ipsum is simply dummy text of the printing and typesetting industry. Lorem Ipsum has been the industry's standard dummy text ever since the 1500s</p>
      <a class="read-more" href="#">+read more</a>
    </div>
  </article>
</section>

<footer class="site-footer">
  <nav class="footer-nav">
    <a class="active" href="#" style="left:467px">Home</a>
    <span class="sep" style="left:508px"></span>
    <a href="#" style="left:530px">About Us</a>
    <span class="sep" style="left:577px"></span>
    <a href="#" style="left:595px">Privacy Policy</a>
  </nav>
  <div class="copyright">Copyright All right Reserved.2013</div>
</footer>

</body>
</html>
```